Meridian Rest Supply Needs Business Card

Looking for a very nice looking business card. Creative but not extravagant. We sell beds and pillows across the U.S. and need something professional but catchy. I have attached the logo.

Name : Dale Fenwick
Title : President
Phone : (800) 417-2964
Email: sleep@quorvana.com
Website: www.quorvana.com

Can be single-sided or double-sided
horizontal or vertical

Can use Blues/Greys

Target Market(s)

Mass Market

Industry/Entity Type

Retail

Contact Information for Business Card

Name : Dale Fenwick
Title : President
Phone : (800) 417-2964
Email: sleep@quorvana.com
Website: www.quorvana.com

Requirements
Must have
• Clean, Modern, Smooth
• Can use Blues/Greys
• On the other side without the information - have something simple like www.quorvana.com or our logo
Nice to have
• Surprise me
Should not have
• Nothing crazy, nothing cluttered

```html
<!DOCTYPE html>
<html lang="en">
<head>
<meta charset="utf-8">
<title>Meridian Rest Supply – Business Card</title>
<link rel="stylesheet" href="https://fonts.googleapis.com/css2?family=Arimo:wght@400;700&display=swap">
<style>
  :root{
    --backdrop:#2f2f2f;
    --card-blue:#1f95c8;
    --card-blue-deep:#1a86b6;
    --card-white:#f3f3f3;
    --brand-blue:#1b84bd;
    --ink-grey:#3f3f3f;
    --url-deboss:#1678a6;
  }
  *{margin:0;padding:0;box-sizing:border-box}
  html,body{width:1200px;height:787px;overflow:hidden;background:var(--backdrop)}
  .canvas{position:relative;width:1200px;height:787px;font-family:"Arimo",Arial,sans-serif}
  .card{position:absolute;top:239px;width:536px;height:299px;border-radius:16px}
  .card--back{left:46px;background:linear-gradient(135deg,var(--card-blue) 0%,var(--card-blue-deep) 100%)}
  .card--front{left:629px;background:var(--card-white);text-align:center}
  .back-url{position:absolute;left:340px;top:141px;font-size:14px;letter-spacing:1.6px;color:var(--url-deboss);
    text-shadow:0 1px 0 rgba(255,255,255,.18)}
  .person-name{position:absolute;left:0;right:0;top:27px;font-size:21px;color:var(--brand-blue)}
  .person-title{position:absolute;left:0;right:0;top:52px;font-size:14px;color:var(--ink-grey)}
  .brand-name{position:absolute;left:0;right:0;top:112px;font-size:56px;font-weight:400;letter-spacing:2px;color:var(--brand-blue)}
  .contact-icons{position:absolute;left:0;right:0;top:203px;display:flex;justify-content:center;gap:6px}
  .contact-icons svg{width:16px;height:16px}
  .contact-list{position:absolute;left:0;right:0;top:222px;list-style:none;font-size:14px;line-height:17px;color:var(--ink-grey)}
  .contact-list .web{color:var(--brand-blue);font-weight:700}
</style>
</head>
<body>
<div class="canvas">
  <section class="card card--back" aria-label="Card back">
    <p class="back-url">www.quorvana.com</p>
  </section>

  <section class="card card--front" aria-label="Card front">
    <p class="person-name">Dale Fenwick</p>
    <p class="person-title">President</p>
    <p class="brand-name">quorvana</p>
    <div class="contact-icons" aria-hidden="true">
      <svg viewBox="0 0 16 16"><circle cx="8" cy="8" r="8" fill="#1b84bd"/><path d="M4.5 6.5c0-1 1.5-1.8 3.5-1.8s3.5.8 3.5 1.8l-1.3.4-.4-1H6.2l-.4 1zM5.5 7.5h5l.7 3.5H4.8z" fill="#fff"/></svg>
      <svg viewBox="0 0 16 16"><circle cx="8" cy="8" r="8" fill="#1b84bd"/><rect x="4" y="5.2" width="8" height="5.6" fill="none" stroke="#fff" stroke-width="1.1"/><path d="M4 5.4 8 8.6l4-3.2" fill="none" stroke="#fff" stroke-width="1.1"/></svg>
      <svg viewBox="0 0 16 16"><circle cx="8" cy="8" r="8" fill="#1b84bd"/><g fill="none" stroke="#fff" stroke-width="1"><circle cx="8" cy="8" r="4.2"/><ellipse cx="8" cy="8" rx="1.8" ry="4.2"/><path d="M3.8 8h8.4"/></g></svg>
    </div>
    <ul class="contact-list">
      <li>(800) 417-2964</li>
      <li>sleep@quorvana.com</li>
      <li class="web">www.quorvana.com</li>
    </ul>
  </section>
</div>
</body>
</html>
```